Business Card Design

I need a business card design for a photography business that specializes in headshots and portraits.

Target Market(s)

Business professionals, actors, actresses

Industry/Entity Type

Business

Contact Information for Business Card

Corvin Lane Photography, Greg Wilmot, 1187 Kestrel Avenue, Suite 416, Fort Wayne, IN 46815, 260.555.0148, www.corvinlanephoto.example. greg.wilmot@corvinlanephoto.example

Requirements
Must have
• The business card should state the type of photography services offered: headshots and portraits.

```html
<!DOCTYPE html>
<html lang="en">
<head>
<meta charset="utf-8">
<title>Corvin Lane Photography – Business Card</title>
<link href="https://fonts.googleapis.com/css2?family=PT+Sans:wght@400;700&display=swap" rel="stylesheet">
<style>
  :root {
    --page-bg: #ffffff;
    --card-bg: #090a09;
    --text-light: #dfe2e0;
    --accent-yellow: #f2dc1a;
    --brand-red: #8e0d0b;
  }
  html, body {
    margin: 0;
    padding: 0;
    width: 1200px;
    height: 1000px;
    overflow: hidden;
    background: var(--page-bg);
  }
  .business-card {
    position: absolute;
    left: 60px;
    top: 183px;
    width: 1082px;
    height: 632px;
    background: var(--card-bg);
    font-family: "PT Sans", "Myriad Pro", sans-serif;
    color: var(--text-light);
  }
  .brand-mark {
    position: absolute;
    top: 110px;
    left: 0;
    width: 100%;
    display: flex;
    justify-content: center;
    align-items: center;
    gap: 16px;
  }
  .brand-mark__dot {
    width: 26px;
    height: 26px;
    border-radius: 50%;
    background: var(--brand-red);
  }
  .brand-mark__name {
    font-size: 44px;
    font-weight: 700;
    color: var(--brand-red);
    letter-spacing: 0.5px;
  }
  .studio-name {
    position: absolute;
    top: 262px;
    left: 0;
    width: 100%;
    margin: 0;
    text-align: center;
    font-size: 70px;
    font-weight: 400;
    line-height: 1;
    white-space: nowrap;
  }
  .studio-name__lead { color: var(--text-light); }
  .studio-name__accent { color: var(--accent-yellow); }
  .services {
    position: absolute;
    top: 372px;
    left: 0;
    width: 100%;
    margin: 0;
    text-align: center;
    font-size: 34px;
    font-weight: 700;
    line-height: 1;
  }
  .contact {
    position: absolute;
    top: 504px;
    left: 0;
    width: 100%;
    margin: 0;
    text-align: center;
    font-size: 23px;
    font-weight: 700;
    line-height: 38px;
    white-space: nowrap;
  }
  .contact__sep { padding: 0 4px; }
  .contact__sep--wide { padding: 0 14px; }
</style>
</head>
<body>
  <section class="business-card">
    <div class="brand-mark">
      <span class="brand-mark__dot"></span>
      <span class="brand-mark__name">Corvin Lane</span>
    </div>

    <h1 class="studio-name">
      <span class="studio-name__lead">Corvin Lane</span>
      <span class="studio-name__accent">Photography</span>
    </h1>

    <p class="services">Headshots &amp; Portraits</p>

    <address class="contact" style="font-style: normal;">
      Greg Wilmot<span class="contact__sep">|</span>1187 Kestrel Avenue, Suite 416, Fort Wayne, IN 46815<span class="contact__sep">|</span>260.555.0148<br>
      www.corvinlanephoto.example<span class="contact__sep contact__sep--wide">|</span>greg.wilmot@corvinlanephoto.example
    </address>
  </section>
</body>
</html>
```